Wohnhof am Weiher - Zeitungsinserat für den Verkauf von Eigentumswohnungen

Wir brauchen ein Zeitungsinserat in zwei Formaten. Einmal 296 Breite x 440 Höhe mm und einmal 296 Breite x 220 mm Höhe.
Als Basis dient der sehr grobe Entwurf im Powerpoint (Entwurf.pptx).
Auf dem Entwurf fehlen noch die Kontaktangeben:
Brunnhofer Liegenschaften AG
Seematteweg 14
4387 Tannried
079 462 37 58
rbrunnhofer@tessin-ostwald.ch

Zudem muss noch der Link auf die Webseite aufgeführt werden.
www.wohnhof-am-weiher.ch

Zudem fehlt noch der Text:
Fordern Sie noch heute die Verkaufsunterlagen gedruckt oder per Email an. Schreiben Sie uns einfach eine Chatpost mit Ihrer Adresse.

Ich habe noch Files von den Innenvisualisierungen, den Aussenvisualisierungen sowie unser Logo hinzugefügt. Zudem habe ich Ihnen die Verkaufsbrochure angefügt. Sie können die Daten vom Entwurf gerne ergänzen wenn Ihnen etwas gefällt. Schön wäre es, wenn Sie den Stil ähnlich machen würden wie die Brochure.

Target Market(s)

Famillien, Paare und Rentner

Font styles to use
Serif

Colors

Designer to choose colors to be used in the design.

Requirements
Must have
• Tolles Design das sofort anspricht!

```html
<!DOCTYPE html>
<html lang="de">
<head>
<meta charset="utf-8">
<title>Wohnhof am Weiher – Inserat</title>
<link href="https://fonts.googleapis.com/css2?family=Open+Sans:wght@600;700;800&family=Roboto:wght@400;500&display=swap" rel="stylesheet">
<style>
  :root{
    --blue:#0a8fd8;
    --navy:#0f2a3a;
    --red:#e0192b;
    --ink:#1d1d1d;
    --body:#444;
    --cell:#dcdcdc;
    --teal:#0f6a86;
    --white:#fff;
  }
  html,body{margin:0;padding:0;overflow:hidden;}
  body{width:808px;height:1200px;position:relative;background:var(--white);font-family:'Roboto',sans-serif;color:var(--ink);}
  .abs{position:absolute;}
  .hero-visual{left:0;top:0;width:808px;height:316px;
    background:linear-gradient(180deg,#eef1f3 0%,#dfe4e6 40%,#b9c2c0 58%,#7ea46a 75%,#5d8a4a 100%);}
  .draft-stamp{left:424px;top:18px;transform:rotate(-4deg);border:3px solid #c8262e;color:#c8262e;
    font-family:'Open Sans',sans-serif;font-weight:800;font-size:26px;letter-spacing:1px;padding:0 8px;line-height:38px;}
  .title-shadow{left:39px;top:230px;width:716px;height:122px;background:var(--navy);}
  .title-band{left:54px;top:216px;width:716px;height:122px;background:var(--blue);text-align:center;}
  .title-band h1{margin:14px 0 0;font-family:'Open Sans',sans-serif;font-weight:700;font-size:49px;color:var(--white);line-height:62px;letter-spacing:.3px;}
  .title-band p{margin:0;font-family:'Open Sans',sans-serif;font-weight:700;font-size:19px;color:var(--red);letter-spacing:.6px;}

  .feature{position:absolute;}
  .feature .tick{position:absolute;left:-56px;top:-10px;}
  .feature h2{margin:0 0 8px;font-family:'Open Sans',sans-serif;font-weight:700;font-size:14px;line-height:17px;color:var(--ink);}
  .feature p{margin:0;font-size:10px;line-height:15.6px;color:var(--body);text-align:justify;}

  .gallery-band{left:0;top:682px;width:808px;height:180px;background:var(--blue);}
  .interior{position:absolute;top:24px;width:231px;height:131px;}
  .i1{left:34px;background:linear-gradient(135deg,#f2f2f0,#d9d6d0 60%,#b9b3aa);}
  .i2{left:290px;background:linear-gradient(135deg,#ecebe8,#cfcac3 55%,#c79a62);}
  .i3{left:545px;background:linear-gradient(135deg,#f6f6f5,#e2e1de 60%,#c4c2bf);}

  .house{position:absolute;top:878px;width:218px;}
  .house h3{margin:0 0 10px;text-align:center;font-family:'Open Sans',sans-serif;font-weight:700;font-size:20px;line-height:24px;}
  .house table{border-collapse:collapse;width:218px;table-layout:fixed;}
  .house td{background:var(--cell);border:1.5px solid var(--white);font-size:7px;line-height:8.2px;vertical-align:top;padding:3px 3px;color:#222;}
  .house tr.r1 td{height:26px}
  .house tr.r2 td,.house tr.r3 td{height:17px}
  .house tr.r4 td{height:35px}
  .house tr.r5 td{height:32px}

  .cta{left:48px;top:1082px;width:713px;text-align:center;font-size:10.5px;line-height:14px;color:var(--body);}
  .cta strong{color:var(--ink);font-weight:500;}

  .brand{left:96px;top:1118px;width:180px;text-align:center;color:var(--teal);font-family:'Open Sans',sans-serif;font-weight:700;}
  .brand .n1{font-size:20px;letter-spacing:1.5px;line-height:24px;}
  .brand .n2{font-size:10px;letter-spacing:2.5px;line-height:14px;}
  .divider{width:2px;height:54px;background:var(--blue);top:1112px;}
  .address{left:330px;top:1109px;width:188px;text-align:center;font-size:19px;line-height:30px;color:var(--ink);}
  .contact{left:568px;top:1107px;}
  .contact .phone{font-family:'Open Sans',sans-serif;font-weight:700;font-size:22px;color:var(--red);line-height:28px;}
  .contact .mail{font-size:10px;color:var(--blue);line-height:15px;}
  .contact .web{font-size:11.5px;color:var(--teal);line-height:16px;}
</style>
</head>
<body>
  <div class="abs hero-visual" role="img" aria-label="Aussenvisualisierung der Wohnsiedlung mit Rasen, Bäumen und Radfahrer"></div>
  <div class="abs draft-stamp">ENTWURF</div>

  <div class="abs title-shadow"></div>
  <div class="abs title-band">
    <h1>Wohnhof am Weiher</h1>
    <p>Hochwertige und moderne Eigentumswohnungen</p>
  </div>

  <svg width="0" height="0" style="position:absolute">
    <defs>
      <symbol id="tick" viewBox="0 0 40 40">
        <circle cx="20" cy="20" r="18" fill="none" stroke="#0a8fd8" stroke-width="2.4"/>
        <path d="M12 20 l6 6 l11 -12" fill="none" stroke="#e0192b" stroke-width="2.6" stroke-linecap="round" stroke-linejoin="round"/>
      </symbol>
    </defs>
  </svg>

  <div class="feature" style="left:139px;top:379px;width:258px;">
    <svg class="tick" width="38" height="38"><use href="#tick"/></svg>
    <h2>Bus und Bahn</h2>
    <p>Der Bahnhof von Riedbach mit Zugverbindungen nach Basel (20 Minuten) und Delemont ist in wenigen Minuten mit dem Bus zu erreichen.</p>
  </div>
  <div class="feature" style="left:139px;top:471px;width:258px;">
    <svg class="tick" width="38" height="38"><use href="#tick"/></svg>
    <h2>Basel – Stadt</h2>
    <p>Der nahegelegene Bahnhof in Riedbach verfügt über sehr gute Verbindungen nach Basel (20 Minuten), welche durch den Doppelspurausbau in den kommenden Jahren sogar noch weiter verbessert werden.</p>
  </div>
  <div class="feature" style="left:139px;top:577px;width:258px;">
    <svg class="tick" width="38" height="38"><use href="#tick"/></svg>
    <h2>Autobahn</h2>
    <p>Die Wohnsiedlung ist ideal auch für den Individualverkehr erschlossen. Die Entfernung zur Autobahn J18 beträgt 12km und ist über Aesch innerhalb von 15 Minuten erreichbar.</p>
  </div>
  <div class="feature" style="left:470px;top:379px;width:258px;">
    <svg class="tick" width="38" height="38"><use href="#tick"/></svg>
    <h2>Einkaufen und weitere Dienstleistungen</h2>
    <p>Durch die Nähe der Gemeindegrenze zwischen Riedbach und Tannried liegen die Dorfzentren mit ihren Einkaufsmöglichkeiten (z.B. Auen Center Riedbach sowie der Altstadt in Riedbach) und Dienstleistungsangeboten in max. 2 Minuten Fahrtzeit oder in 10-15 Minuten Gehdistanz.</p>
  </div>
  <div class="feature" style="left:470px;top:541px;width:258px;">
    <svg class="tick" width="38" height="38"><use href="#tick"/></svg>
    <h2>Erholung im Grünen</h2>
    <p>Tannried erfüllt mit seinen Wäldern, dem eigenen «Dorfberg» dem «Stürmenkopf», den offenen Feldern, den Wander- und Velorouten und der ländlichen Ruhe alle Voraussetzungen, die ein Naherholungsgebiet begehrt machen.</p>
  </div>

  <div class="abs gallery-band">
    <div class="interior i1" role="img" aria-label="Innenvisualisierung: offene Küche mit Essbereich"></div>
    <div class="interior i2" role="img" aria-label="Innenvisualisierung: Wohnzimmer mit Sofa und Küche"></div>
    <div class="interior i3" role="img" aria-label="Innenvisualisierung: heller Essbereich mit rundem Tisch"></div>
  </div>

  <div class="house" style="left:48px;">
    <h3>Haus A</h3>
    <table>
      <colgroup><col style="width:36px"><col style="width:42px"><col style="width:30px"><col style="width:60px"><col style="width:50px"></colgroup>
      <tr class="r1"><td>Attika</td><td>4.5<br>Zimmer</td><td>108m²</td><td>105m²<br>Sonnenterrasse</td><td>945'000 CHF</td></tr>
      <tr class="r2"><td>Oberges<br>choss</td><td>3.5<br>Zimmer</td><td>81m²</td><td>16m² Balkon</td><td>754'800 CHF</td></tr>
      <tr class="r3"><td>Oberges<br>choss</td><td>4.5<br>Zimmer</td><td>102m²</td><td>33m² Balkon</td><td>640'000 CHF</td></tr>
      <tr class="r4"><td>Erdgesc<br>hoss</td><td>3.5<br>Zimmer</td><td>81m²</td><td>16m²<br>gedeckter<br>Sitzplatz &amp;<br>eigener Garten</td><td>657'000 CHF</td></tr>
      <tr class="r5"><td>Erdgesc<br>hoss</td><td>4.5<br>Zimmer</td><td>102m²</td><td>33m²<br>gedeckter<br>Sitzplatz &amp;<br>eigener Garten</td><td>765'000 CHF</td></tr>
    </table>
  </div>

  <div class="house" style="left:294px;">
    <h3>Haus B</h3>
    <table>
      <colgroup><col style="width:36px"><col style="width:42px"><col style="width:30px"><col style="width:60px"><col style="width:50px"></colgroup>
      <tr class="r1"><td>Attika</td><td>4.5<br>Zimmer</td><td>109m²</td><td>107m²<br>Sonnenterrasse</td><td>965'000 CHF</td></tr>
      <tr class="r2"><td>Oberges<br>choss</td><td>2.5<br>Zimmer</td><td>69m²</td><td>14m² Balkon</td><td>550'000 CHF</td></tr>
      <tr class="r3"><td>Oberges<br>choss</td><td>4.5<br>Zimmer</td><td>117m²</td><td>42m² Balkon</td><td>877'500 CHF</td></tr>
      <tr class="r4"><td>Erdgesc<br>hoss</td><td>2.5<br>Zimmer</td><td>69m²</td><td>14m²<br>gedeckter<br>Sitzplatz &amp;<br>eigener Garten</td><td>560'000 CHF</td></tr>
      <tr class="r5"><td>Erdgesc<br>hoss</td><td>4.5<br>Zimmer</td><td>117m²</td><td>42m²<br>gedeckter<br>Sitzplatz &amp;<br>eigener Garten</td><td>889'000 CHF</td></tr>
    </table>
  </div>

  <div class="house" style="left:540px;width:221px;">
    <h3>Haus C</h3>
    <table style="width:221px;">
      <colgroup><col style="width:36px"><col style="width:42px"><col style="width:30px"><col style="width:60px"><col style="width:53px"></colgroup>
      <tr class="r1"><td>Attika</td><td>4.5<br>Zimmer</td><td>129m²</td><td>132m²<br>Sonnenterrasse</td><td>1'125'000 CHF</td></tr>
      <tr class="r2"><td>Oberges<br>choss</td><td>5.5<br>Zimmer</td><td>143m²</td><td>43m² Balkon</td><td>1'058'000 CHF</td></tr>
      <tr class="r3"><td>Oberges<br>choss</td><td>3.5<br>Zimmer</td><td>96m²</td><td>23m² Balkon</td><td>730'500 CHF</td></tr>
      <tr class="r4"><td>Erdgesc<br>hoss</td><td>5.5<br>Zimmer</td><td>143m²</td><td>43m²<br>gedeckter<br>Sitzplatz &amp;<br>eigener Garten</td><td>1'065'000 CHF</td></tr>
      <tr class="r5"><td>Erdgesc<br>hoss</td><td>3.5<br>Zimmer</td><td>96m²</td><td>23m²<br>gedeckter<br>Sitzplatz &amp;<br>eigener Garten</td><td>740'000 CHF</td></tr>
    </table>
  </div>

  <p class="abs cta" style="margin:0;"><strong>Fordern Sie noch heute die Verkaufsunterlagen gedruckt oder per Email an.</strong> Schreiben Sie uns einfach eine Chatpost mit Ihrer Adresse.</p>

  <div class="abs brand">
    <div class="n1">BRUNNHOFER</div>
    <div class="n2">LIEGENSCHAFTEN AG</div>
  </div>
  <div class="abs divider" style="left:322px;"></div>
  <div class="abs address">Seematteweg 14<br>4387 Tannried</div>
  <div class="abs divider" style="left:526px;"></div>
  <div class="abs contact">
    <div class="phone">079 462 37 58</div>
    <div class="mail">rbrunnhofer@tessin-ostwald.ch</div>
    <div class="web">www.wohnhof-am-weiher.ch</div>
  </div>
</body>
</html>
```